Creative, Colorful, Dynamic Infographic for Global Non-Profit

We are a global arts and education non-profit in need of an infographic that illustrates four key skills embedded in our work: Curiosity, Listening, Imagination, Postive Action.
We work primarily with educators, students, and artists who use the power of personal stories to build community and connection and to bridge divides.
Our new brand guidelines, logos, and fonts are here: https://stylekit.example/quillbridge-7
I've attached a mock-up of the graphic and the required text. (Note the attached design was created by a staff person, your final design does not need to be the same. The color scheme and text of the final design should match the brand guidelines above.)
The graphic will be used for both web and print media and should include the purple Quillbridge 7 logo (also attached).
Ideally the final design will delight audiences and spark interest in our work.

```html
<!DOCTYPE html>
<html lang="en">
<head>
<meta charset="utf-8">
<title>Quillbridge 7 – Four Skills Infographic</title>
<link rel="stylesheet" href="https://fonts.googleapis.com/css2?family=Arimo:wght@400&family=Libre+Baskerville:wght@700&display=swap">
<style>
  :root {
    --curiosity: #6a2c91;
    --positive-action: #4db58f;
    --listening: #1f63c1;
    --imagination: #e8474a;
    --hub: #1f1c3a;
    --bridge: #e5f0fa;
    --bridge-text: #1f1c3a;
    --ring-light: #f4f4f4;
    --ring-dark: #c9c9c9;
    --paper: #ffffff;
  }
  html, body {
    margin: 0;
    padding: 0;
    width: 1200px;
    height: 733px;
    overflow: hidden;
    background: var(--paper);
  }
  .infographic {
    display: block;
    width: 1200px;
    height: 733px;
  }
  .skill-title {
    font-family: "Libre Baskerville", Georgia, serif;
    font-weight: 700;
    font-size: 14px;
    fill: #ffffff;
    text-anchor: middle;
  }
  .skill-text {
    font-family: "Arimo", Arial, sans-serif;
    font-size: 8.6px;
    fill: #ffffff;
    text-anchor: middle;
  }
  .bridge-text {
    font-family: "Arimo", Arial, sans-serif;
    font-size: 8.4px;
    fill: var(--bridge-text);
    text-anchor: middle;
  }
  .hub-name {
    font-family: "Libre Baskerville", Georgia, serif;
    font-weight: 700;
    font-size: 12px;
    fill: #ffffff;
    text-anchor: middle;
  }
  .bridge { fill: var(--bridge); }
  .node-ring { fill: none; stroke: #ffffff; stroke-width: 2; }
</style>
</head>
<body>
<svg class="infographic" viewBox="0 0 940 573" xmlns="http://www.w3.org/2000/svg" role="img" aria-label="Quillbridge 7 four skills: Curiosity, Positive action, Imagination and Listening">
  <defs>
    <linearGradient id="petal-shade" gradientUnits="userSpaceOnUse" x1="-110" y1="-110" x2="-25" y2="-25">
      <stop offset="0" stop-color="#000" stop-opacity="0"/>
      <stop offset="1" stop-color="#000" stop-opacity="0.5"/>
    </linearGradient>
    <radialGradient id="ring-metal" cx="0.4" cy="0.35" r="0.7">
      <stop offset="0" stop-color="var(--ring-light)"/>
      <stop offset="0.75" stop-color="#e6e6e6"/>
      <stop offset="1" stop-color="var(--ring-dark)"/>
    </radialGradient>
    <filter id="soft-shadow" x="-20%" y="-200%" width="140%" height="500%">
      <feGaussianBlur stdDeviation="5"/>
    </filter>
    <filter id="ring-shadow" x="-30%" y="-30%" width="160%" height="160%">
      <feDropShadow dx="0" dy="2" stdDeviation="3" flood-color="#000" flood-opacity="0.25"/>
    </filter>

    <path id="petal" d="M -67,-130 Q -58,-76 0,-58 L -58,0 Q -78,-58 -129,-68 Z"/>

    <g id="bridges">
      <rect class="bridge" x="-63" y="-162" width="132" height="50"/>
      <text class="bridge-text" x="3" y="-142">Your positive actions lead</text>
      <text class="bridge-text" x="3" y="-131">to curiosity about what</text>
      <text class="bridge-text" x="3" y="-120">else is possible</text>

      <rect class="bridge" x="-153" y="-64" width="22" height="130"/>
      <text class="bridge-text" transform="translate(-143,1) rotate(-90)" y="-1">Your curiosity</text>
      <text class="bridge-text" transform="translate(-143,1) rotate(-90)" y="8.5">allows you to listen</text>

      <rect class="bridge" x="131" y="-64" width="22" height="130"/>
      <text class="bridge-text" transform="translate(143,1) rotate(-90)" y="-1">Your imagination</text>
      <text class="bridge-text" transform="translate(143,1) rotate(-90)" y="8.5">can spark positive action</text>

      <rect class="bridge" x="-56" y="116" width="120" height="42"/>
      <text class="bridge-text" x="4" y="134">Your listening allows you to</text>
      <text class="bridge-text" x="4" y="145">take in new information</text>
    </g>

    <g id="petals">
      <use href="#petal" fill="var(--curiosity)"/>
      <use href="#petal" fill="var(--positive-action)" transform="scale(-1,1)"/>
      <use href="#petal" fill="var(--listening)" transform="scale(1,-1)"/>
      <use href="#petal" fill="var(--imagination)" transform="scale(-1,-1)"/>
    </g>

    <g id="petal-shading">
      <use href="#petal" fill="url(#petal-shade)"/>
      <use href="#petal" fill="url(#petal-shade)" transform="scale(-1,1)"/>
      <use href="#petal" fill="url(#petal-shade)" transform="scale(1,-1)"/>
      <use href="#petal" fill="url(#petal-shade)" transform="scale(-1,-1)"/>
    </g>

    <g id="nodes">
      <g class="skill skill-curiosity" transform="translate(-129,-130)">
        <circle r="62" fill="var(--curiosity)"/>
        <circle class="node-ring" r="55"/>
        <text class="skill-title" y="-24">Curiosity</text>
        <text class="skill-text" y="-7">Focus on how you</text>
        <text class="skill-text" y="4">can learn from</text>
        <text class="skill-text" y="15">another’s knowledge</text>
        <text class="skill-text" y="26">and experience</text>
      </g>
      <g class="skill skill-positive-action" transform="translate(129,-130)">
        <circle r="62" fill="var(--positive-action)"/>
        <circle class="node-ring" r="55"/>
        <text class="skill-title" y="-8">Positive action</text>
        <text class="skill-text" y="9">Show your words</text>
        <text class="skill-text" y="20">and actions matter</text>
      </g>
      <g class="skill skill-listening" transform="translate(-129,130)">
        <circle r="62" fill="var(--listening)"/>
        <circle class="node-ring" r="55"/>
        <text class="skill-title" y="-8">Listening</text>
        <text class="skill-text" y="9">Seek to understand</text>
        <text class="skill-text" y="20">before speaking</text>
      </g>
      <g class="skill skill-imagination" transform="translate(129,130)">
        <circle r="62" fill="var(--imagination)"/>
        <circle class="node-ring" r="55"/>
        <text class="skill-title" y="-12">Imagination</text>
        <text class="skill-text" y="5">Consider</text>
        <text class="skill-text" y="16">possibilities beyond</text>
        <text class="skill-text" y="27">what you know</text>
      </g>
      <g class="hub">
        <circle r="57" fill="var(--hub)"/>
        <text class="hub-name" y="4">Quillbridge 7</text>
      </g>
    </g>
  </defs>

  <!-- Flat version -->
  <g class="variant variant-flat">
    <ellipse cx="238" cy="520" rx="145" ry="6" fill="#000" opacity="0.18" filter="url(#soft-shadow)"/>
    <g transform="translate(231,282)">
      <use href="#bridges"/>
      <use href="#petals"/>
      <use href="#nodes"/>
    </g>
  </g>

  <!-- Dimensional version -->
  <g class="variant variant-dimensional">
    <ellipse cx="694" cy="520" rx="145" ry="6" fill="#000" opacity="0.18" filter="url(#soft-shadow)"/>
    <g transform="translate(691,282)">
      <use href="#bridges"/>
      <use href="#petals"/>
      <use href="#petal-shading"/>
      <g class="rings" fill="url(#ring-metal)" filter="url(#ring-shadow)">
        <circle cx="-129" cy="-130" r="71"/>
        <circle cx="129" cy="-130" r="71"/>
        <circle cx="-129" cy="130" r="71"/>
        <circle cx="129" cy="130" r="71"/>
        <circle cx="0" cy="0" r="67"/>
      </g>
      <use href="#nodes"/>
    </g>
  </g>
</svg>
</body>
</html>
```